CD cover design, a Flag for the "Lumen Harbor"

CD cover design needed for the release of a new single called "Lumen Harbor" by www.pelatrask.com. The idea is a flag, the flag of the "Lumen Harbor" the song is about a reinvented Utopia, a perfect social political economical organization, a place where we all want to belong to and feel safe and free, controlled technology, restaured humanity, opportunity, no tolerance for crime. To be celebrated it in every performance.

```html
<!DOCTYPE html>
<html lang="en">
<head>
<meta charset="utf-8">
<title>Lumen Harbor — Pela Trask</title>
<link rel="stylesheet" href="https://fonts.googleapis.com/css2?family=Open+Sans:wght@400&display=swap">
<style>
  :root {
    --white: #ffffff;
    --flag-grey: rgba(200, 205, 215, 0.55);
    --mark-grey: rgba(200, 200, 200, 0.8);
    --red: #d8141e;
    --magenta: #e4206e;
    --orange: #f08a1c;
    --yellow: #e4dc1e;
    --green: #1eb43a;
    --teal: #10b4a6;
    --blue: #1e46b0;
    --deep: #1a1030;
  }
  html, body {
    margin: 0;
    padding: 0;
    width: 1200px;
    height: 1200px;
    overflow: hidden;
    background: var(--deep);
  }
  .cover {
    position: relative;
    width: 1200px;
    height: 1200px;
    overflow: hidden;
    font-family: "Open Sans", Arial, sans-serif;
  }
  .cover-art {
    position: absolute;
    inset: 0;
    background:
      radial-gradient(ellipse 420px 260px at 620px 420px, rgba(200,16,24,0.9), rgba(200,16,24,0) 70%),
      linear-gradient(160deg, rgba(240,138,28,0.9) 0%, rgba(228,32,110,0.75) 18%, rgba(30,70,176,0.7) 32%, rgba(216,20,30,0.85) 46%, rgba(16,180,166,0.8) 62%, rgba(30,180,58,0.85) 78%, rgba(228,220,30,0.85) 100%),
      linear-gradient(20deg, var(--magenta) 0%, var(--teal) 50%, var(--red) 100%);
  }
  .flag {
    position: absolute;
    left: 0;
    top: 0;
    width: 1200px;
    height: 1200px;
  }
  .flag-pole { stroke: var(--flag-grey); stroke-width: 10; stroke-linecap: round; }
  .flag-cloth { fill: var(--flag-grey); }
  .label-mark {
    position: absolute;
    left: 990px;
    top: 90px;
    width: 120px;
    height: 120px;
    border-radius: 50%;
    background: var(--mark-grey);
  }
  .release-title {
    position: absolute;
    left: 0;
    right: 0;
    top: 545px;
    margin: 0;
    text-align: center;
    font-size: 130px;
    font-weight: 400;
    letter-spacing: 5px;
    line-height: 1;
    color: var(--white);
    text-transform: uppercase;
    white-space: nowrap;
  }
  .artist-name {
    position: absolute;
    left: 0;
    right: 0;
    top: 1107px;
    margin: 0;
    text-align: center;
    font-size: 57px;
    font-weight: 400;
    letter-spacing: 2px;
    line-height: 1;
    color: var(--white);
    text-transform: uppercase;
    white-space: nowrap;
  }
</style>
</head>
<body>
  <main class="cover">
    <div class="cover-art" role="img" aria-label="Vivid painted abstract of a figure raising a flag amid bold strokes of red, magenta, green, teal, yellow and blue"></div>
    <svg class="flag" viewBox="0 0 1200 1200" aria-hidden="true">
      <line class="flag-pole" x1="592" y1="104" x2="702" y2="420"/>
      <path class="flag-cloth" d="M600 118 C660 96 720 138 790 112 C830 98 860 104 880 112 C860 160 850 210 870 262 C820 250 780 270 740 284 C700 296 670 290 648 272 Z"/>
    </svg>
    <div class="label-mark" aria-hidden="true"></div>
    <h1 class="release-title">Lumen Harbor</h1>
    <p class="artist-name">Pela Trask</p>
  </main>
</body>
</html>
```